New Web-Page Design Required

We need a new or initial web design for our page vorlan-grid.com. We provide products & services around infrastructure products. We have two products at the moment, but another 2 in the pipeline.
We want to have the following page structure (and part of the project is to design the 7 pages):
- Home
- Products
-One page per product
- Service
- Support
- About
- Contact (Email form)
The start page should include the following information:
- Twitter / Linkedin Links
- Telephone / Email or in general contact details
- News
- Maybe a link-box, where we can highlight/showcase things
- Link to our support portal, quite prominent
- Testimonials
It would be nice if the product pages would have a image header, where we can put up a screenshot or something. Links to datasheet and videos of the product would be nice as well.
We like the "big banner in the middle" designs, like these two Joomla examples. No need to copy them, it should just give you an idea.
http://www.pelmorthemes.com/itempreview/185
http://www.pelmorthemes.com/content/asj42/index.php
Budget for images available, so please use placeholders or ask us for specific photos/images, if you need them for your design.
Target Market(s)
Business-2-Business, Decision makers and Technical Leads
Industry/Entity Type
News
Look and feel

```html
<!DOCTYPE html>
<html lang="en">
<head>
<meta charset="utf-8">
<title>Vorlan-Grid</title>
<link href="https://fonts.googleapis.com/css2?family=Fjalla+One&family=Open+Sans:ital,wght@0,400;0,600;1,400&display=swap" rel="stylesheet">
<style>
:root{
  --teal:#13a9b6;
  --teal-bright:#19bfcc;
  --dark:#252223;
  --dark-2:#2f2c2d;
  --paper:#f1f1f1;
  --band:#dddddd;
  --tab-grey:#6e6e6e;
  --ink:#222;
  --ink-soft:#444;
  --quote-mark:#777;
  --white:#fff;
}
*{box-sizing:border-box;margin:0;padding:0}
html,body{width:1118px;height:1200px;overflow:hidden}
body{position:relative;background:var(--paper);font-family:"Open Sans",sans-serif;color:var(--ink)}
.abs{position:absolute}
.display{font-family:"Fjalla One",sans-serif;font-weight:400}

/* header */
.site-header{left:0;top:0;width:1118px;height:103px;background:linear-gradient(135deg,#f6f6f6,#ececec)}
.brand{left:168px;top:11px;width:169px;height:85px;background:var(--white);border:3px solid #cfcfcf;display:flex;align-items:center;justify-content:center;gap:8px}
.brand-dot{width:24px;height:24px;border-radius:50%;background:var(--teal)}
.brand-name{font-weight:600;font-size:20px;color:#4a4a4a}
.contact-lines{left:766px;top:29px;font-size:11.5px;line-height:14px;color:#111}
.social{left:766px;top:62px;display:flex;gap:6px}
.social span{width:25px;height:25px;border:2px solid #cfcfcf;background:var(--teal)}

/* nav */
.main-nav{left:0;top:103px;width:1118px;height:38px;background:#ececec;border-top:1px solid #c9c9c9;border-bottom:1px solid #d6d6d6}
.nav-home{left:168px;top:0;width:46px;height:37px;background:var(--dark);display:flex;align-items:center;justify-content:center}
.nav-item{top:0;height:37px;display:flex;align-items:center;justify-content:center;font-family:"Fjalla One",sans-serif;font-size:12px;letter-spacing:1px;color:#222;border-right:1px solid #c4c4c4}

/* hero */
.hero{left:0;top:141px;width:1118px;height:335px;background:var(--dark)}
.hero-photo{left:168px;top:141px;width:548px;height:335px;background:linear-gradient(100deg,#f4f4f4 0%,#ecebea 40%,#9a8178 52%,#efefef 72%)}
.hero-rule{left:0;top:476px;width:1118px;height:6px;background:var(--teal)}
.slide-tabs{left:716px;top:141px;display:flex}
.slide-tab{width:46px;height:46px;display:flex;align-items:center;justify-content:center;color:var(--white);font-size:22px;background:var(--tab-grey)}
.slide-tab.is-active{background:var(--teal);position:relative}
.slide-tab.is-active::after{content:"";position:absolute;left:0;top:46px;border-left:23px solid transparent;border-right:23px solid transparent;border-top:13px solid var(--teal)}
.hero-title{left:727px;top:223px;width:168px;font-size:23px;line-height:34px;color:var(--white);letter-spacing:1px;text-align:center}
.hero-title span{display:block;text-align:left}
.hero-title span:first-child{text-align:center;padding-right:18px}
.hero-text{left:728px;top:325px;width:164px;font-size:12.5px;line-height:17.5px;color:var(--white)}

/* columns */
.col-head{top:529px;width:184px;height:38px;background:linear-gradient(90deg,#e4e4e4,#d9d9d9);font-size:15.5px;letter-spacing:1px;padding:9px 0 0 8px;color:#222}
.resource-list{left:168px;top:572px;width:184px;height:254px;background:var(--dark-2);padding:12px 10px;color:var(--white);box-shadow:0 1px 3px rgba(0,0,0,.3)}
.resource-list li{list-style:none;margin-bottom:14px}
.resource-list b{display:block;font-weight:400;font-size:13.5px;letter-spacing:.3px}
.resource-list b::before{content:"› ";font-weight:600}
.resource-list small{display:block;font-size:10.5px;line-height:14px;letter-spacing:.5px;padding-right:14px}
.support-photo{left:367px;top:572px;width:184px;height:116px;background:linear-gradient(110deg,#d8d9da,#efe6df 40%,#c9c9cb);border:1px solid #cfcfcf}
.support-box{left:367px;top:696px;width:184px;height:129px;background:var(--teal-bright);padding:12px 6px;font-size:10.5px;line-height:13.5px;letter-spacing:.3px;color:#102a2c}
.btn{display:inline-block;margin-top:10px;background:var(--white);font-family:"Fjalla One",sans-serif;font-size:11.5px;letter-spacing:1px;padding:3px 8px;color:#222}
.news{left:569px;top:575px;width:164px}
.news-item{margin-bottom:16px}
.news-item h3{font-family:"Fjalla One",sans-serif;font-weight:400;font-size:12.5px}
.news-item time{display:block;font-size:9.5px;margin:1px 0 5px}
.news-item p{font-size:9.5px;line-height:14px;letter-spacing:.3px;color:var(--ink-soft)}
.quote{width:184px;height:108px;background:var(--dark-2);border-radius:10px;padding:26px 20px 0 30px;color:var(--white);box-shadow:0 2px 4px rgba(0,0,0,.35)}
.quote::before{content:"“";position:absolute;left:16px;top:2px;font-family:Georgia,serif;font-size:40px;color:var(--quote-mark)}
.quote p{font-style:italic;font-size:11px;line-height:14px;letter-spacing:.5px}
.quote cite{display:block;font-style:normal;font-weight:600;font-size:11px;margin-top:8px;letter-spacing:.5px}
.quote::after{content:"";position:absolute;left:88px;top:106px;border-left:26px solid transparent;border-top:16px solid var(--dark-2)}

/* gallery */
.gallery{left:0;top:870px;width:1118px;height:246px;background:var(--band);border-top:1px solid #c9c9c9}
.gallery-label{left:218px;top:878px;width:92px;height:30px;background:var(--dark);color:var(--white);font-size:17px;letter-spacing:1px;text-align:center;line-height:30px}
.shot{top:942px;width:151px;height:110px;background:linear-gradient(180deg,#3a3f42,#23282b);box-shadow:0 2px 4px rgba(0,0,0,.4)}

/* footer */
.site-footer{left:0;top:1116px;width:1118px;height:84px;background:var(--dark);color:var(--white);text-align:center;font-size:12.5px;line-height:21px;padding-top:24px}
</style>
</head>
<body>

<header class="abs site-header">
  <div class="abs brand"><span class="brand-dot"></span><span class="brand-name">vorlan-grid</span></div>
  <div class="abs contact-lines">Phone- 0000 5555 7777<br>Email-&nbsp; info@vorlan-grid.com</div>
  <div class="abs social"><span role="img" aria-label="Professional network link"></span><span role="img" aria-label="Microblog link"></span></div>
</header>

<nav class="abs main-nav">
  <div class="abs nav-home">
    <svg width="18" height="16" viewBox="0 0 18 16"><path d="M9 1 L17 8 H14 V15 H11 V10 H7 V15 H4 V8 H1 Z" fill="#13a9b6"/></svg>
  </div>
  <div class="abs nav-item" style="left:214px;width:99px">PRODUCTS</div>
  <div class="abs nav-item" style="left:313px;width:101px">SERVICE</div>
  <div class="abs nav-item" style="left:414px;width:107px">SUPPORT</div>
  <div class="abs nav-item" style="left:521px;width:98px">ABOUT</div>
  <div class="abs nav-item" style="left:619px;width:97px">CONTACT</div>
</nav>

<section class="abs hero"></section>
<div class="abs hero-photo" role="img" aria-label="Photo of a businesswoman working on a laptop in a bright office"></div>
<div class="abs slide-tabs">
  <div class="slide-tab is-active">1</div><div class="slide-tab">2</div><div class="slide-tab">3</div><div class="slide-tab">4</div>
</div>
<h1 class="abs hero-title display"><span>EASY</span><span>ADMINISTRATION</span></h1>
<p class="abs hero-text display">Our goal is to provide flexibility, but no administration overhead. The m.Ledger administration gives you just enough.</p>
<div class="abs hero-rule"></div>

<h2 class="abs col-head display" style="left:168px">VIDEOS &amp; DATASHEETS</h2>
<h2 class="abs col-head display" style="left:367px">SUPPORT</h2>
<h2 class="abs col-head display" style="left:566px">NEWS</h2>
<h2 class="abs col-head display" style="left:765px">TESTIMONIALS</h2>

<ul class="abs resource-list">
  <li><b>m.Ledger</b><small>Dynamic video about our m.Ledger application.</small></li>
  <li><b>m.Ledger Datasheet</b><small>Download the m.Ledger Datasheet.</small></li>
  <li><b>CCD/C</b><small>CCD/C Feature Presentation</small></li>
  <li><b>CCD/C Datasheet</b><small>Download the CCD/C Datasheet</small></li>
</ul>

<div class="abs support-photo" role="img" aria-label="Photo of a smiling support agent wearing a headset"></div>
<div class="abs support-box">
  We provide several levels of support for our software and we do not follow strict support levels. You decide, what level of support you need.
  <br><span class="btn">READ MORE</span>
</div>

<div class="abs news">
  <article class="news-item">
    <h3>CCD/C Released</h3><time>2013-05-21</time>
    <p>Vorlan-Grid has released the first version of the Cirrova Cloud Director Collector for Halvern Lumen4Ops. The collector is natively integrated into the Lumen4Ops installation and comes with a rich set of reports.</p>
  </article>
  <article class="news-item">
    <h3>CCD/C Released</h3><time>2013-05-21</time>
    <p>A Pocketa version of m.Ledger for Lumen4Ops will be released in August. You will see the same great features as in the Pocketa Touch version.</p>
  </article>
</div>

<blockquote class="abs quote" style="left:765px;top:576px"><p>Lorem ipsum dolor sit amet, consectetur adipisicing...</p><cite>Aloe Doe</cite></blockquote>
<blockquote class="abs quote" style="left:767px;top:712px"><p>Lorem ipsum dolor sit amet, consectetur adipisicing...</p><cite>John Doe</cite></blockquote>

<section class="abs gallery"></section>
<div class="abs gallery-label display">GALLERY</div>
<svg class="abs" style="left:168px;top:980px" width="18" height="26" viewBox="0 0 18 26"><path d="M14 2 L4 13 L14 24" fill="none" stroke="#555" stroke-width="3"/></svg>
<svg class="abs" style="left:932px;top:980px" width="18" height="26" viewBox="0 0 18 26"><path d="M4 2 L14 13 L4 24" fill="none" stroke="#555" stroke-width="3"/></svg>
<div class="abs shot" style="left:218px" role="img" aria-label="Screenshot of an events dashboard with a bar chart"></div>
<div class="abs shot" style="left:394px" role="img" aria-label="Screenshot of a device summary report"></div>
<div class="abs shot" style="left:571px" role="img" aria-label="Screenshot of an inventory report with a pie chart"></div>
<div class="abs shot" style="left:747px" role="img" aria-label="Screenshot of a network summary report"></div>

<footer class="abs site-footer">
  Copyright © 2013 Vorlan-Grid<br>
  Halvern, Lumen4Ops are either registered trademarks or trademarks of Halvern Corporation in the United States and/or other countries.
</footer>

</body>
</html>
```